Business card for auto dealership

Looking for a clean modern design.
Would like attached logo incorporated

Industry/Entity Type

Car dealership

Contact Information for Business Card

Name, website, phone, cell, fax, email

```html
<!DOCTYPE html>
<html lang="en">
<head>
<meta charset="utf-8">
<title>Halvorsen Truck &amp; Auto Sales – Business Card</title>
<link rel="stylesheet" href="https://fonts.googleapis.com/css2?family=Montserrat:wght@400;600&family=Niconne&display=swap">
<style>
  :root {
    --backdrop: #d9d9d9;
    --card-light: #ffffff;
    --card-dark: #060607;
    --ink: #161616;
    --ink-soft: #3a3a3a;
    --silver: #bdbdbd;
    --rule: #2a2a2a;
  }
  * { box-sizing: border-box; margin: 0; padding: 0; }
  html, body {
    width: 1200px; height: 1200px; overflow: hidden;
    background: var(--backdrop);
  }
  .canvas { position: relative; width: 1200px; height: 1200px; }
  .card {
    position: absolute; left: 152px; width: 894px; height: 524px;
    box-shadow: 0 2px 6px rgba(0,0,0,0.25);
  }
  .card--front { top: 59px; background: var(--card-light); color: var(--ink); }
  .card--back { top: 610px; background: var(--card-dark); }

  .brand {
    position: absolute; left: 0; right: 0; text-align: center;
    font-family: "Montserrat", sans-serif; font-weight: 600;
    line-height: 1;
  }
  .brand__name { display: block; font-size: 88px; letter-spacing: 1px; }
  .brand__tagline { display: block; font-size: 24px; letter-spacing: 2px; margin-top: 12px; text-transform: uppercase; }
  .card--front .brand { top: 82px; color: var(--ink); }
  .card--back .brand { top: 178px; color: var(--silver); }

  .divider {
    position: absolute; left: 82px; width: 728px; top: 284px;
    height: 2px; background: var(--rule);
  }
  .person-name {
    position: absolute; right: 86px; top: 318px;
    font-family: "Niconne", cursive; font-size: 60px; line-height: 1;
    color: var(--ink);
  }
  .contact-list {
    position: absolute; list-style: none;
    font-family: "Montserrat", sans-serif; font-weight: 400;
    font-size: 21px; color: var(--ink-soft); letter-spacing: 0.5px;
  }
  .contact-list--phones { left: 82px; top: 372px; }
  .contact-list--online { left: 478px; top: 407px; }
  .contact-list li { display: flex; align-items: center; height: 34.5px; }
  .contact-icon { width: 16px; height: 16px; margin-right: 14px; fill: var(--ink); flex: none; }
</style>
</head>
<body>
<div class="canvas">

  <section class="card card--front">
    <div class="brand">
      <span class="brand__name">Halvorsen</span>
      <span class="brand__tagline">Truck &amp; Auto Sales</span>
    </div>
    <div class="divider"></div>
    <div class="person-name">Daniel Marsh</div>

    <ul class="contact-list contact-list--phones">
      <li>
        <svg class="contact-icon" viewBox="0 0 16 16" aria-hidden="true"><path d="M5 1h6a1 1 0 0 1 1 1v12a1 1 0 0 1-1 1H5a1 1 0 0 1-1-1V2a1 1 0 0 1 1-1zm.5 1.5v10h5v-10z"/></svg>
        555-210-0000
      </li>
      <li>
        <svg class="contact-icon" viewBox="0 0 16 16" aria-hidden="true"><path d="M4 2l2.2 2.6-1.3 1.6c.9 2 2.6 3.7 4.6 4.6l1.6-1.3L14 12l-1.6 2C7 13.6 2.4 9 2 3.6z"/></svg>
        555-210-1212
      </li>
      <li>
        <svg class="contact-icon" viewBox="0 0 16 16" aria-hidden="true"><path d="M4 1h6l2 2v3H4zM1 7h14v7H1zm3 4v3h8v-3z"/></svg>
        555-210-2222
      </li>
    </ul>

    <ul class="contact-list contact-list--online">
      <li>
        <svg class="contact-icon" viewBox="0 0 16 16" aria-hidden="true"><path d="M1 4h14v9H1zm1.5 1L8 9l5.5-4z" fill-rule="evenodd"/></svg>
        office@halvorsenauto.com
      </li>
      <li>
        <svg class="contact-icon" viewBox="0 0 16 16" aria-hidden="true"><circle cx="8" cy="8" r="6.5" fill="none" stroke="currentColor" stroke-width="1.6"/><path d="M1.5 8h13M8 1.5c2.5 3 2.5 10 0 13M8 1.5c-2.5 3-2.5 10 0 13" fill="none" stroke="currentColor" stroke-width="1.2"/></svg>
        www.halvorsenauto.com
      </li>
    </ul>
  </section>

  <section class="card card--back">
    <div class="brand">
      <span class="brand__name">Halvorsen</span>
      <span class="brand__tagline">Truck &amp; Auto Sales</span>
    </div>
  </section>

</div>
</body>
</html>
```